Renamed Motel Needs Appealing Flyer

We need a flyer design for a motel that has been closed for 3 years and has just reopened under new management. It has been renamed 'Tallowind Motel' and is located in the Grampians in Vic. We would like our design to showcase the beauty and magnificence of the Grampians National Park (Gariwerd being the Aboriginal name for the Park). The motel is an older style building, so we don't want photos of the building to be the focus of the flyer until we have had time to renovate etc.
http://www.filedrovex.com/file/9tq2pm
I will add a high res image of the motel name/logo on Monday
http://www.filedrovex.com/file/9tq2pm to see an additional photo. I will add a high res image of motel name/logo on Monday
all ages, backpackers, budget consious travellers, seniors, groups
- Flyer must be DL size (front and back only) with logo at the top so that it is visible when displayed in a tiered display rack. I am not sure if the logo I have provided is adequate resolution wise. Can you let me know if it is not? The 'points' under the name are not part of the logo and should be removed.
Suggested wording for front of flyer - Surrounded by rugged mountain ranges and native plants and animals, Tallowind Motel is the perfect base to explore the natural beauty of the Grampians.
Back of flyer - features: affordable accommodation, 25 spacious ground floor rooms,
single/twin/triple/quadruple rooms; queen beds; ensuite bathrooms/some rooms with baths; toaster/ tea and coffee making facilities; iron/ironing board in rooms; digital TV; free WiFi; microwaves for guest use; free BBQ facilities; breakfast available; conference facility for up to 25 persons
Address - 14 Brackley Rd, Mossvale 3274
Phone: (03) 5471 2098
Email: tallowindmotel@quokmail.com
www.tallowindmotel.com.au
Updated after first set of submissions/comments - 10.55 PM AEST.
The following text only should be for the front of the brochure - Surrounded by rugged mountain ranges and native plants and animals, Tallowind Motel is the perfect base to explore the natural beauty of the Grampians.
Logically then, listings from the original brief such as 'Surrounded by mountains' would not be relevant for the back.
The dot points listed above in the first brief, should then be the focus for the information and detail on the back of the brochure.
Another update is;
- correct display is R/Trak
- I would like the flyer to have a flowing feel, print over top of scenery images, different fonts. Perhaps back of flyer could be printed over a washed image of Grampians

```html
<!DOCTYPE html>
<html lang="en">
<head>
<meta charset="utf-8">
<title>Tallowind Motel – DL Flyer</title>
<link rel="stylesheet" href="https://fonts.googleapis.com/css2?family=PT+Sans:ital,wght@0,400;0,700;1,400;1,700&family=Roboto+Condensed:wght@700&display=swap">
<style>
  :root {
    --forest: #1b4a24;
    --forest-deep: #163d1d;
    --lime: #8cc63f;
    --gold: #e6c21d;
    --cream: #f6f1c9;
    --white: #ffffff;
    --ink: #111611;
    --backdrop: #ece7df;
  }
  * { margin: 0; padding: 0; box-sizing: border-box; }
  html, body { width: 1200px; height: 1155px; overflow: hidden; }
  body {
    background: var(--backdrop);
    font-family: "PT Sans", "Helvetica Neue", Arial, sans-serif;
    position: relative;
  }
  .panel {
    position: absolute;
    top: 51px;
    width: 484px;
    height: 1027px;
    overflow: hidden;
    box-shadow: 0 4px 14px rgba(0,0,0,0.25);
  }
  .panel--front { left: 105px; }
  .panel--back { left: 627px; }
  .panel__art { position: absolute; inset: 0; width: 100%; height: 100%; display: block; }

  /* Front */
  .brand-name {
    position: absolute; left: 0; right: 0; top: 48px;
    text-align: center;
    font-weight: 700;
    font-size: 50px;
    color: var(--cream);
    letter-spacing: 0.5px;
  }
  .front-heading {
    position: absolute; left: 54px; top: 702px;
    font-family: "Roboto Condensed", "Arial Narrow", sans-serif;
    font-weight: 700; font-size: 29px;
    color: var(--lime);
  }
  .front-points { list-style: none; }
  .front-points li {
    position: absolute; left: 52px; right: 20px;
    font-weight: 700; font-size: 23px; line-height: 28px;
    color: var(--white);
  }
  .front-points li::before {
    content: ""; position: absolute; left: -52px; top: 9px;
    width: 36px; height: 12px; background: var(--gold);
  }

  /* Back */
  .back-title {
    position: absolute; left: 38px; top: 74px;
    font-family: "Roboto Condensed", "Arial Narrow", sans-serif;
    font-weight: 700; font-size: 34px; color: var(--gold);
  }
  .back-subtitle {
    position: absolute; left: 40px; top: 118px;
    font-weight: 700; font-size: 22px; letter-spacing: 3px; color: var(--white);
  }
  .facility-list { list-style: none; }
  .facility-list li {
    position: absolute; left: 74px; right: 20px;
    font-weight: 700; font-size: 23px; line-height: 30px; color: var(--white);
  }
  .facility-list li::before {
    content: ""; position: absolute; left: -38px; top: 9px;
    width: 0; height: 0;
    border-top: 7px solid transparent;
    border-bottom: 7px solid transparent;
    border-left: 12px solid var(--white);
  }
  .contact {
    position: absolute; left: 0; right: 0; top: 838px;
    text-align: center; color: var(--ink);
  }
  .contact__name {
    font-family: "Roboto Condensed", "Arial Narrow", sans-serif;
    font-weight: 700; font-size: 32px; line-height: 38px;
  }
  .contact__address { font-weight: 700; font-size: 17px; margin-top: 4px; }
  .contact__line { font-size: 17px; font-weight: 700; line-height: 24px; }
  .contact__line em { font-style: italic; }
  .contact__phone { margin-top: 22px; }
  .contact__web {
    font-weight: 700; font-size: 17px; letter-spacing: 4px; margin-top: 14px;
  }
</style>
</head>
<body>

<section class="panel panel--front">
  <svg class="panel__art" viewBox="0 0 377 800" preserveAspectRatio="none" aria-hidden="false">
    <defs>
      <linearGradient id="familyPhotoTone" x1="0" y1="0" x2="1" y2="1">
        <stop offset="0" stop-color="#e9dccb"/>
        <stop offset="0.45" stop-color="#d9b79a"/>
        <stop offset="0.8" stop-color="#a9b98a"/>
        <stop offset="1" stop-color="#7f9a6a"/>
      </linearGradient>
    </defs>
    <rect width="377" height="800" fill="var(--forest)"/>
    <path d="M0,168 C110,140 260,150 377,178 L377,260 L0,260 Z" fill="var(--gold)"/>
    <path role="img" aria-label="Photo of a smiling family of four outdoors"
          d="M0,186 C110,160 260,170 377,196 L377,470 C290,500 180,516 0,520 Z"
          fill="url(#familyPhotoTone)"/>
    <path d="M150,520 C250,500 330,470 377,430 L377,448 C330,490 250,515 150,520 Z" fill="var(--lime)"/>
    <path d="M90,522 C230,515 320,480 377,452 L377,478 C310,505 220,522 90,522 Z" fill="var(--gold)"/>
  </svg>

  <div class="brand-name">Tallowind Motel</div>

  <h2 class="front-heading">Tallowind Motel</h2>
  <ul class="front-points">
    <li style="top:756px">Surrounded by the mountains,</li>
    <li style="top:801px">Motel is an easy 5 minute walk from the centre of Mossvale,</li>
    <li style="top:876px">100 metres from R/Trak bus stop</li>
    <li style="top:920px">Affordable accommodation</li>
    <li style="top:963px">25 spacious ground floor rooms</li>
  </ul>
</section>

<section class="panel panel--back">
  <svg class="panel__art" viewBox="0 0 377 800" preserveAspectRatio="none" aria-hidden="true">
    <rect width="377" height="800" fill="var(--forest)"/>
    <path d="M60,16 C190,8 320,38 377,66 L377,112 C320,62 210,26 60,16 Z" fill="var(--gold)"/>
    <path d="M160,30 C250,40 335,78 377,112 L377,140 C330,94 255,52 160,30 Z" fill="var(--lime)"/>
    <path d="M0,540 C110,600 270,610 377,568 L377,580 C270,625 110,615 0,565 Z" fill="var(--lime)"/>
    <path d="M0,575 C120,628 270,630 377,592 L377,800 L0,800 Z" fill="var(--lime)"/>
  </svg>

  <h2 class="back-title">Tallowind Motel</h2>
  <div class="back-subtitle">FACILITIES</div>

  <ul class="facility-list">
    <li style="top:158px">Single / Twin / Triple /<br>Quadruple Rooms</li>
    <li style="top:227px">Queen beds</li>
    <li style="top:267px">Ensuite bathrooms /<br>some rooms with baths</li>
    <li style="top:337px">Toaster/ Tea &amp; coffee making<br>facilities</li>
    <li style="top:406px">Iron / Ironing board in rooms</li>
    <li style="top:446px">Digital TV</li>
    <li style="top:485px">Free WiFi</li>
    <li style="top:525px">Microwaves for guest use</li>
    <li style="top:565px">Free BBQ facilities</li>
    <li style="top:603px">Breakfast available</li>
    <li style="top:643px">Conference facility for up to<br>25 persons</li>
  </ul>

  <address class="contact" style="font-style:normal">
    <div class="contact__name">Tallowind Motel</div>
    <div class="contact__address">14 Brackley Rd, Mossvale 3274</div>
    <div class="contact__line contact__phone"><em>Phone:</em> (03) 5471 2098</div>
    <div class="contact__line"><em>Email:</em> tallowindmotel@quokmail.com</div>
    <div class="contact__web">www.tallowindmotel.com.au</div>
  </address>
</section>

</body>
</html>
```